Restaurant Email Club Sign Up Poster

Looking for a creative design that will catch people's eye and prompt them to sign up for our email club for our Restaurant that we run in Omaha, Nebraska. Open to any creative ways to most effectively grab peoples attention quickly without being too confusing. Want it to be simple but actionable.

Have attached some documents for your assistance - in addition to some marketing materials we have put out in the past.

Would like to put design on posters to hang up throughout the restaurant and likely will make stickers to put on check presenters as well.

Catchy stock photo or use of the cheese curd photo probably good idea - callout things mentioned in the "must haves" section below. Looking for most creative and catchy, yet simple design.

Target Market(s)

30-50 year olds males and females.

Industry/Entity Type

Restaurant

Requirements
Must have
• Must include callouts for -
• Sign up for E-Club for access to future offers and events (or something along these lines)
• Free Appetizer for Signing Up
• Free Birthday Meal
Should not have
• Please do not make this poster like the postcard that I attached to the project - this is not a poster to call out that we are a new burger and beer spot, that we have 40 rotating taps, or that we have 15 specialty burgers, etc. This is simply a poster to grab someones attention and get them to sign up for our email club. Should maybe have a catchy question, something like, "Want a Free Appetizer?" or something catchy and similar, and then below say "And access to future deals and event happenings?"

```html
<!DOCTYPE html>
<html lang="en">
<head>
<meta charset="utf-8">
<title>E-Club Sign Up Poster</title>
<link rel="stylesheet" href="https://fonts.googleapis.com/css2?family=Montserrat:wght@800&family=Roboto+Slab:wght@700&family=Open+Sans:wght@600&display=swap">
<style>
  :root {
    --poster-green: #99ba0b;
    --ink-white: #ffffff;
    --ink-dark: #161616;
    --rule-white: rgba(255,255,255,0.9);
    --shadow: rgba(40,55,0,0.55);
    --milk: #f3f5f2;
    --herb: #4f8f1c;
    --curd: #e9dc8a;
    --egg: #e48a5c;
    --fried: #c8521d;
    --pepper: #2a2420;
  }
  * { margin: 0; padding: 0; box-sizing: border-box; }
  html, body { width: 900px; height: 1200px; overflow: hidden; }
  body { background: var(--poster-green); }
  .poster {
    position: relative;
    width: 900px;
    height: 1200px;
    background: var(--poster-green);
    overflow: hidden;
    color: var(--ink-white);
  }
  .food {
    position: absolute;
  }
  .food--milk { left: 410px; top: 140px; width: 190px; height: 180px; border-radius: 50% 40% 55% 45%;
    background: radial-gradient(ellipse at 50% 45%, var(--milk) 0%, rgba(230,235,230,0.85) 55%, rgba(230,235,230,0) 75%); }
  .food--parsley { left: 720px; top: 235px; width: 75px; height: 80px; border-radius: 50%;
    background: radial-gradient(circle, var(--herb) 0%, rgba(79,143,28,0.8) 55%, rgba(79,143,28,0) 75%); }
  .food--dill { left: 170px; top: 415px; width: 120px; height: 125px; border-radius: 50%;
    background: radial-gradient(circle, #3d7a1e 0%, rgba(61,122,30,0.7) 50%, rgba(61,122,30,0) 72%); }
  .food--curds { left: 365px; top: 395px; width: 170px; height: 75px; border-radius: 40%;
    background: linear-gradient(180deg, #f1e6a0, var(--curd) 60%, #d8c56c); }
  .food--egg { left: 600px; top: 390px; width: 115px; height: 165px; border-radius: 50% 50% 48% 48% / 58% 58% 42% 42%;
    background: radial-gradient(ellipse at 40% 35%, #f2a57c, var(--egg) 55%, #c86c40); }
  .food--fried { left: 215px; top: 580px; width: 485px; height: 150px; border-radius: 30px;
    background: radial-gradient(ellipse at 45% 55%, #f0a020 0%, var(--fried) 45%, rgba(160,60,20,0.85) 70%, rgba(160,60,20,0) 90%); }
  .food--pepper { left: 215px; top: 850px; width: 165px; height: 110px; border-radius: 50%;
    background: radial-gradient(ellipse at 30% 35%, var(--pepper) 0%, rgba(42,36,32,0.55) 40%, rgba(42,36,32,0) 70%); }

  .kicker {
    position: absolute; top: 58px; left: 0; width: 900px; text-align: center;
    font-family: "Roboto Slab", serif; font-size: 36px; letter-spacing: 1px;
    text-shadow: 3px 4px 6px var(--shadow);
  }
  .headline {
    position: absolute; left: 0; top: 160px; width: 900px;
    font-family: "Montserrat", sans-serif; font-weight: 800;
    font-size: 113px; line-height: 143px;
    text-shadow: 6px 8px 10px var(--shadow);
  }
  .headline span { display: block; white-space: nowrap; }
  .headline .l1 { padding-left: 198px; }
  .headline .l2 { padding-left: 132px; }
  .headline .l3 { padding-left: 238px; }

  .benefit-copy {
    position: absolute; top: 605px; left: 0; width: 890px; text-align: center;
    font-family: "Roboto Slab", serif; font-size: 36px; line-height: 60.5px; letter-spacing: 0.5px;
    text-shadow: 3px 4px 6px var(--shadow);
  }

  .perk { position: absolute; text-align: center; }
  .perk--appetizer {
    left: 148px; top: 914px; width: 277px; height: 114px;
    border-top: 2px solid var(--rule-white); border-bottom: 2px solid var(--rule-white);
    font-family: "Roboto Slab", serif; font-size: 29px; line-height: 36px; padding-top: 16px;
    text-shadow: 2px 3px 5px var(--shadow);
  }
  .perk--birthday {
    left: 103px; top: 1070px; width: 365px; height: 69px;
    border-top: 2px solid var(--rule-white); border-bottom: 2px solid var(--rule-white);
    font-family: "Open Sans", sans-serif; font-weight: 600; font-size: 29px; line-height: 65px;
    text-shadow: 2px 3px 5px var(--shadow);
  }

  .brand {
    position: absolute; left: 520px; top: 985px; width: 280px;
    display: flex; align-items: center; gap: 14px;
    font-family: "Roboto Slab", serif; font-size: 34px; line-height: 40px;
    color: var(--ink-dark);
  }
  .brand-mark { width: 34px; height: 34px; background: var(--ink-dark); flex: none; }
</style>
</head>
<body>
<main class="poster">
  <div class="food food--milk" role="img" aria-label="Splash of milk"></div>
  <div class="food food--parsley" role="img" aria-label="Sprig of parsley"></div>
  <div class="food food--dill" role="img" aria-label="Sprig of dill"></div>
  <div class="food food--curds" role="img" aria-label="Pile of fresh cheese curds"></div>
  <div class="food food--egg" role="img" aria-label="Brown egg"></div>
  <div class="food food--fried" role="img" aria-label="Golden fried cheese curds"></div>
  <div class="food food--pepper" role="img" aria-label="Scattered black peppercorns"></div>

  <p class="kicker">GET A FREE APPETIZER</p>

  <h1 class="headline">
    <span class="l1">SIGN UP</span>
    <span class="l2">FOR OUR</span>
    <span class="l3">E-CLUB</span>
  </h1>

  <p class="benefit-copy">TO GAIN ACCESS TO<br>INFORMATION ABOUT<br>FUTURE OFFERS AND<br>EXCLUSIVE EVENTS.</p>

  <p class="perk perk--appetizer">FREE APPETIZER<br>FOR SIGNING UP</p>
  <p class="perk perk--birthday">FREE BIRTHDAY MEAL</p>

  <div class="brand">
    <span class="brand-mark"></span>
    <span class="brand-name">PRAIRIE<br>TAP ROOM</span>
  </div>
</main>
</body>
</html>
```